Keystone Renewal
Cards and Stationary
Project: Keystone Renewal
Keystone Renewal - Environment
Creative Brief
Professional
Tim Hollister
Operations Manager
27 Marrow Lane Florence, Ky 41057
Tim@krflow.com
krflow.com
24/7 Emergency Water Removal Services
Pure Guild Certified in *Water Damage Restoration * Applied Structural Drying *Applied Microbial Remediation *Carpet Cleaning * Odor Control* Nrb Lead Safe Renovator * Level One Thermographer
Concepts
Business Cards, Letterhead, and Envelopes

```html
<!DOCTYPE html>
<html lang="en">
<head>
<meta charset="utf-8">
<title>Keystone Renewal – Business Card</title>
<link rel="stylesheet" href="https://fonts.googleapis.com/css2?family=Arimo:ital,wght@0,400;0,700;1,400&display=swap">
<style>
  :root {
    --backdrop: #e9e4de;
    --card-black: #080808;
    --name-bar: #3a3a3a;
    --brand-blue: #2f8fd0;
    --brand-green: #6cbf3a;
    --text-white: #ffffff;
    --text-grey: #b9b9b9;
    --swoosh-dark: #0b3f78;
    --swoosh-light: #2f8fd0;
    --swoosh-line: #d9d9d9;
  }
  * { margin: 0; padding: 0; box-sizing: border-box; }
  html, body { width: 1200px; height: 367px; overflow: hidden; }
  body {
    background: var(--backdrop);
    font-family: "Arimo", Arial, sans-serif;
    position: relative;
  }
  .card {
    position: absolute;
    top: 29px;
    width: 530px;
    height: 307px;
    border-radius: 22px;
    background: var(--card-black);
    overflow: hidden;
    color: var(--text-white);
  }
  .card--front { left: 53px; }
  .card--back { left: 617px; }

  .name-bar {
    position: absolute; top: 14px; left: 0; right: 0; height: 30px;
    background: var(--name-bar);
    display: flex; align-items: center; gap: 14px;
    padding-left: 70px; font-size: 15px;
  }
  .name-bar .divider { color: var(--text-grey); }
  .name-bar .role { font-size: 12px; }

  .brand {
    position: absolute; left: 0; right: 0;
    display: flex; align-items: center; justify-content: center; gap: 14px;
  }
  .card--front .brand { top: 62px; }
  .card--back .brand { top: 60px; }
  .brand__mark {
    width: 52px; height: 52px; border-radius: 50%;
    background: var(--brand-blue);
  }
  .brand__name {
    color: var(--brand-blue); font-weight: 700;
    font-size: 34px; line-height: 1; letter-spacing: 1px;
    text-transform: uppercase;
  }

  .tagline {
    position: absolute; top: 166px; left: 0; right: 0; text-align: center;
    color: var(--brand-green); font-style: italic; font-size: 15px;
  }
  .contact {
    position: absolute; left: 48px; top: 192px;
    font-size: 13px; line-height: 24px;
  }
  .contact span + span { margin-left: 14px; }

  .swoosh { position: absolute; left: 0; bottom: 0; width: 530px; height: 80px; }
  .card--front .web {
    position: absolute; right: 40px; bottom: 18px;
    font-size: 13px; letter-spacing: 1px;
  }

  .cert-title {
    position: absolute; top: 158px; left: 0; right: 0; text-align: center;
    color: var(--brand-green); font-style: italic; font-size: 15px;
  }
  .cert-list {
    position: absolute; top: 186px; left: 60px; right: 40px;
    list-style: none;
    display: grid; grid-template-columns: 1fr 1fr; column-gap: 14px; row-gap: 7px;
    color: var(--text-grey); font-size: 12px;
  }
  .cert-list li::before { content: "•"; margin-right: 8px; }
  .cert-list .centered { grid-column: 1 / span 2; padding-left: 90px; }
  .card--back .web {
    position: absolute; bottom: 22px; left: 0; right: 0; text-align: center;
    color: var(--brand-blue); font-size: 13px; letter-spacing: 1px;
  }
</style>
</head>
<body>
  <section class="card card--front">
    <div class="name-bar">
      <span class="name">Tim Hollister</span>
      <span class="divider">|</span>
      <span class="role">Operations Manager</span>
    </div>
    <div class="brand">
      <span class="brand__mark"></span>
      <span class="brand__name">Keystone<br>Renewal</span>
    </div>
    <p class="tagline">24/7 Emergency Water Removal Services</p>
    <div class="contact">
      <p><span>C : 859-555-0142</span><span>E : Tim@krflow.com</span></p>
      <p>27 Marrow Lane, Florence, Ky 41057</p>
    </div>
    <svg class="swoosh" viewBox="0 0 530 80" preserveAspectRatio="none" aria-hidden="true">
      <path d="M0 24 C160 52 340 18 530 10 L530 80 L0 80 Z" fill="var(--swoosh-dark)"/>
      <path d="M0 42 C170 72 340 32 530 26 L530 80 L0 80 Z" fill="var(--swoosh-light)"/>
      <path d="M0 22 C160 50 340 16 530 8" stroke="var(--swoosh-line)" stroke-width="3" fill="none"/>
    </svg>
    <p class="web">www.krflow.com</p>
  </section>

  <section class="card card--back">
    <div class="brand">
      <span class="brand__mark"></span>
      <span class="brand__name">Keystone<br>Renewal</span>
    </div>
    <p class="cert-title">Pure Guild Certified in:</p>
    <ul class="cert-list">
      <li>Water Damage Restoration</li>
      <li>Applied Structural Drying</li>
      <li>Applied Microbial Remediation</li>
      <li>Carpet Cleaning</li>
      <li>Odor Control</li>
      <li>Nrb Lead Safe Renovator</li>
      <li class="centered">Level One Thermographer</li>
    </ul>
    <p class="web">www.krflow.com</p>
  </section>
</body>
</html>
```